Retail Sign for Houseplant Campaign

Sign will measure 3 to 4 foot tall by 22.2inches and place on rolling racks of houseplants for a retail promotion in The Yardwell Mart. The theme of the promotion will be "New Year, New You!" Selling points which should be on the sign are Houseplants give you a taste of nature, Houseplants boost air quality inside your home, Indoor plants reduce anxiety, Indoor plants make you more productive, Houseplants improve your concentration and memory.
Updates

Target Market(s)

People who love plants

Industry/Entity Type

Horticulture/ retail

Colors
00AB8E
00BBA5
67D7C9
C6EFE9
E9F9F6
59FF00
82FF00
B8FF75
E3FFCB
F4FFEA
FFF300
FFF600
FEFA6F
FFFEC7
FFFEE8

Requirements
Must have
• Must feel energetic and encourage people to buy plants. Should include 1-2 photos and the selling points listed

```html
<!DOCTYPE html>
<html lang="en">
<head>
<meta charset="utf-8">
<title>Houseplants benefits – New Year, New You!</title>
<link href="https://fonts.googleapis.com/css2?family=Archivo+Black&family=Yellowtail&display=swap" rel="stylesheet">
<style>
  :root{
    --yellow:#f5ee1f;
    --lime:#97cb3d;
    --title-green:#17492a;
    --icon-ink:#2e3314;
    --white:#ffffff;
  }
  *{margin:0;padding:0;box-sizing:border-box}
  html,body{width:746px;height:1200px;overflow:hidden;background:var(--white)}
  .sign{position:relative;width:746px;height:1200px;overflow:hidden}
  .sign__art{position:absolute;inset:0}
  .sign__title{
    position:absolute;left:380px;top:18px;width:340px;text-align:center;
    font-family:"Archivo Black",sans-serif;font-size:44px;line-height:52px;
    color:var(--title-green);
  }
  .benefit{
    position:absolute;left:529px;
    font-family:"Archivo Black",sans-serif;font-size:19px;line-height:24px;
    color:var(--yellow);text-shadow:0 1px 3px rgba(0,0,0,.35);
  }
  .slogan{
    font-family:"Yellowtail",cursive;font-size:80px;
    fill:var(--white);
  }
</style>
</head>
<body>
<main class="sign">
  <svg class="sign__art" width="746" height="1200" viewBox="0 0 746 1200">
    <defs>
      <linearGradient id="plantPhotoTop" x1="0" y1="0" x2="1" y2="0">
        <stop offset="0" stop-color="#f1ece6"/>
        <stop offset="0.35" stop-color="#e3c3ae"/>
        <stop offset="0.6" stop-color="#4f7a45"/>
        <stop offset="1" stop-color="#1d3d22"/>
      </linearGradient>
      <linearGradient id="livingRoomPhoto" x1="0" y1="0" x2="1" y2="0">
        <stop offset="0" stop-color="#7fa35a"/>
        <stop offset="0.35" stop-color="#eef0ec"/>
        <stop offset="0.7" stop-color="#e9cfc8"/>
        <stop offset="1" stop-color="#c9d2dc"/>
      </linearGradient>
    </defs>

    <rect class="photo photo--care" role="img" aria-label="Smiling woman wiping the leaves of a large monstera plant" x="0" y="0" width="746" height="660" fill="url(#plantPhotoTop)"/>
    <rect class="photo photo--relax" role="img" aria-label="Relaxed woman in a pink sweater sitting by a sofa in a bright living room with houseplants" x="0" y="720" width="746" height="480" fill="url(#livingRoomPhoto)"/>

    <path class="wave wave--title" d="M225 0 C290 70 370 135 470 138 C570 141 650 100 746 92 V0 Z" fill="var(--yellow)"/>
    <path class="wave wave--white" d="M0 470 C60 560 140 625 240 650 L0 660 Z" fill="var(--white)"/>
    <circle cx="12" cy="612" r="66" fill="var(--yellow)"/>

    <path class="band" d="M0 668 C120 662 250 640 380 610 C500 580 600 520 746 500 V786 C680 790 600 776 500 770 C350 762 150 790 0 746 Z" fill="var(--lime)"/>
    <circle cx="657" cy="556" r="21" fill="var(--yellow)"/>
    <circle cx="738" cy="566" r="34" fill="var(--white)"/>
    <circle cx="679" cy="608" r="13" fill="var(--white)"/>
    <circle cx="740" cy="783" r="30" fill="var(--white)"/>

    <text class="slogan" x="48" y="742" textLength="650" lengthAdjust="spacingAndGlyphs" transform="rotate(-5 48 742)">New Year, New You!</text>

    <path class="wave wave--base" d="M0 1140 C200 1160 400 1170 560 1150 C650 1140 710 1118 746 1110 V1200 H0 Z" fill="var(--yellow)"/>
    <circle cx="63" cy="1155" r="28" fill="var(--lime)"/>
    <circle cx="112" cy="1117" r="14" fill="var(--white)"/>

    <g class="benefit-icons" fill="var(--yellow)">
      <circle cx="489" cy="185" r="30"/>
      <circle cx="489" cy="251" r="30"/>
      <circle cx="489" cy="317" r="30"/>
      <circle cx="489" cy="386" r="30"/>
      <circle cx="489" cy="463" r="30"/>
    </g>
    <g class="benefit-glyphs" fill="none" stroke="var(--icon-ink)" stroke-width="1.6" stroke-linecap="round" stroke-linejoin="round">
      <path d="M476 200 H504 M482 200 V186 M482 186 m-6 0 a6 7 0 1 1 12 0 a6 6 0 0 1 -12 0 M494 200 V182 M494 182 m-7 0 a7 9 0 1 1 14 0 a7 7 0 0 1 -14 0"/>
      <path d="M475 243 q7 -5 14 0 t14 0 M475 251 q7 -5 14 0 t14 0 M475 259 q7 -5 14 0 t14 0"/>
      <path d="M480 333 V326 a10 11 0 1 1 19 -4 l3 6 h-3 v4 a3 3 0 0 1 -3 3 h-4 v3 M489 308 v10 M486 318 h6"/>
      <circle cx="489" cy="386" r="11"/>
      <path d="M489 371 v4 M489 397 v4 M474 386 h4 M500 386 h4 M478 375 l3 3 M497 394 l3 3 M478 397 l3 -3 M497 378 l3 -3 M483 388 a6 6 0 0 0 11 0 M483 384 a6 6 0 0 1 11 0"/>
      <path d="M489 450 v26 M489 450 c-6 -3 -13 1 -12 7 c-5 2 -5 9 0 11 c-1 6 6 9 12 8 M489 450 c6 -3 13 1 12 7 c5 2 5 9 0 11 c1 6 -6 9 -12 8 M481 460 h4 M493 466 h4 M482 469 l3 2"/>
    </g>
  </svg>

  <h1 class="sign__title">Houseplants benefits</h1>

  <p class="benefit" style="top:171px">taste of nature</p>
  <p class="benefit" style="top:237px">boost air quality</p>
  <p class="benefit" style="top:303px">reduce anxiety</p>
  <p class="benefit" style="top:360px">make you<br>more productive</p>
  <p class="benefit" style="top:427px">improve your<br>concentration<br>&amp; memory</p>
</main>
</body>
</html>
```